Vendra Q7 - DL Flyer

Flyer designed with the following points:

Retail Point of Sale
Hardware and Software
Highly customisable to suit your business
Free POS appraisal and Quotes
E-commerce Integrations with your existing website
Multiple Store Capability
One on one set up and support
100% Tax Deductable
From only $9.95 per week

1300 462 718
admin@vendraq7.com.au
www.vendraq7.com.au

```html
<!DOCTYPE html>
<html lang="en">
<head>
<meta charset="utf-8">
<title>Vendra Q7 - DL Flyer</title>
<link rel="stylesheet" href="https://fonts.googleapis.com/css2?family=Montserrat:wght@400;500;600;700;800&family=Oswald:wght@600&display=swap">
<style>
  :root {
    --navy: #10273e;
    --blue: #1fa8e0;
    --red: #e84461;
    --white: #ffffff;
    --page: #eeeeee;
    --row-grey: #e6e6e6;
    --row-blue: #e3f1fa;
    --ink: #10273e;
  }
  * { box-sizing: border-box; margin: 0; padding: 0; }
  html, body { width: 1200px; height: 1028px; overflow: hidden; }
  body {
    background: var(--page);
    font-family: "Montserrat", sans-serif;
    color: var(--ink);
    display: flex;
    align-items: center;
    justify-content: center;
    gap: 40px;
  }
  .flyer {
    width: 520px;
    height: 780px;
    position: relative;
    overflow: hidden;
  }

  /* ---------- Back side ---------- */
  .flyer--back { background: var(--navy); color: var(--white); }
  .back-brand {
    text-align: center;
    padding-top: 30px;
    font-size: 46px;
    font-weight: 700;
    color: var(--blue);
    letter-spacing: 2px;
  }
  .product-grid {
    display: grid;
    grid-template-columns: repeat(4, 1fr);
    gap: 18px 14px;
    padding: 22px 26px 0;
  }
  .product-frame {
    height: 72px;
    border: 1.5px solid var(--white);
    border-radius: 5px;
    display: flex;
    align-items: center;
    justify-content: center;
    text-align: center;
    font-size: 9px;
    font-weight: 600;
    line-height: 1.3;
  }
  .product-price {
    text-align: right;
    font-size: 9px;
    font-weight: 600;
    margin-top: 5px;
  }
  .package-grid {
    display: grid;
    grid-template-columns: 1fr 1fr;
    gap: 16px 22px;
    padding: 22px 40px 0;
  }
  .package {
    background: var(--white);
    color: var(--ink);
    height: 150px;
    display: flex;
    flex-direction: column;
    border: 3px solid var(--white);
  }
  .package--foot { flex-direction: column-reverse; }
  .package-head {
    background: var(--blue);
    color: var(--white);
    padding: 5px 8px;
    text-align: center;
  }
  .package-name { font-size: 14px; font-weight: 800; letter-spacing: 1px; line-height: 1.1; }
  .package-sub { font-size: 7px; font-weight: 600; letter-spacing: 2.5px; }
  .package-body { flex: 1; display: flex; flex-direction: column; justify-content: center; }
  .package-price {
    text-align: center;
    font-weight: 800;
    font-size: 30px;
    line-height: 1;
  }
  .package-price sup { font-size: 10px; vertical-align: 14px; }
  .package-price .cur { font-size: 10px; vertical-align: 10px; margin-right: 2px; }
  .package-week { text-align: center; font-size: 10px; margin-bottom: 4px; }
  .package-features { list-style: none; font-size: 8.5px; }
  .package-features li {
    padding: 2px 0 2px 46px;
    display: flex;
    align-items: center;
    gap: 4px;
  }
  .package-features li:nth-child(odd) { background: var(--row-blue); }
  .package-features li:nth-child(even) { background: var(--row-grey); }
  .tick { width: 8px; height: 8px; }
  .back-contact {
    position: absolute;
    left: 0; right: 0; bottom: 0;
    height: 104px;
    background: var(--blue);
    border-top: 4px solid var(--white);
    text-align: center;
    padding-top: 12px;
  }
  .contact-phone { font-size: 34px; font-weight: 500; letter-spacing: 3px; line-height: 1.1; }
  .contact-line { font-size: 14px; letter-spacing: 2px; }

  /* ---------- Front side ---------- */
  .flyer--front { background: var(--white); }
  .front-head {
    height: 140px;
    background: var(--navy);
    border-bottom: 7px solid var(--blue);
    display: flex;
    align-items: center;
    justify-content: center;
  }
  .front-brand {
    font-size: 50px;
    font-weight: 700;
    color: var(--blue);
    letter-spacing: 2px;
  }
  .feature-list {
    list-style: none;
    padding: 44px 40px 0 56px;
  }
  .feature-list li {
    position: relative;
    padding-left: 26px;
    font-size: 19px;
    font-weight: 700;
    letter-spacing: 1.2px;
    line-height: 1.2;
    margin-bottom: 22px;
  }
  .feature-list li::before {
    content: "";
    position: absolute;
    left: 0; top: 6px;
    width: 10px; height: 10px;
    border-radius: 50%;
    background: var(--blue);
  }
  .front-foot {
    position: absolute;
    left: 0; bottom: 0;
    width: 520px; height: 200px;
  }
  .tax-offer {
    position: absolute;
    right: 34px; bottom: 22px;
    text-align: right;
    color: var(--white);
  }
  .tax-figure { font-family: "Oswald", sans-serif; font-weight: 600; font-size: 62px; line-height: 1; }
  .tax-label { font-size: 24px; font-weight: 500; letter-spacing: 4px; }
</style>
</head>
<body>

<section class="flyer flyer--back" aria-label="Flyer back: products and packages">
  <div class="back-brand">VENDRA Q7</div>

  <div class="product-grid">
    <div><div class="product-frame"></div><div class="product-price">Price: $195</div></div>
    <div><div class="product-frame">Image of<br>your Product</div><div class="product-price">Price: $170</div></div>
    <div><div class="product-frame">Image of<br>your Product</div><div class="product-price">Price: $99</div></div>
    <div><div class="product-frame">Image of<br>your Product</div><div class="product-price">Price: $39</div></div>
    <div><div class="product-frame">Image of<br>your Product</div><div class="product-price">Price: $65</div></div>
    <div><div class="product-frame">Image of<br>your Product</div><div class="product-price">Price: $89</div></div>
    <div><div class="product-frame">Image of<br>your Product</div><div class="product-price">Price: $121</div></div>
    <div><div class="product-frame">Image of<br>your Product</div><div class="product-price">Price: $19.99</div></div>
  </div>

  <div class="package-grid">
    <article class="package">
      <div class="package-head"><div class="package-name">SMALL RETAIL</div><div class="package-sub">SOFTWARE PACKAGE</div></div>
      <div class="package-body">
        <div class="package-price"><span class="cur">$</span>9<sup>95</sup></div>
        <div class="package-week">Per Week</div>
        <ul class="package-features">
          <li><svg class="tick" viewBox="0 0 10 10"><circle cx="5" cy="5" r="4.2" fill="none" stroke="#1fa8e0"/><path d="M3 5.2l1.5 1.5L7.3 3.6" fill="none" stroke="#1fa8e0" stroke-width="1.2"/></svg>1-2 Staff Users</li>
          <li><svg class="tick" viewBox="0 0 10 10"><circle cx="5" cy="5" r="4.2" fill="none" stroke="#1fa8e0"/><path d="M3 5.2l1.5 1.5L7.3 3.6" fill="none" stroke="#1fa8e0" stroke-width="1.2"/></svg>1 Cash Register</li>
          <li><svg class="tick" viewBox="0 0 10 10"><circle cx="5" cy="5" r="4.2" fill="none" stroke="#1fa8e0"/><path d="M3 5.2l1.5 1.5L7.3 3.6" fill="none" stroke="#1fa8e0" stroke-width="1.2"/></svg>1 Store Location</li>
        </ul>
      </div>
    </article>

    <article class="package">
      <div class="package-head"><div class="package-name">MEDIUM RETAIL</div><div class="package-sub">SOFTWARE PACKAGE</div></div>
      <div class="package-body">
        <div class="package-price"><span class="cur">$</span>17<sup>95</sup></div>
        <div class="package-week">Per Week</div>
        <ul class="package-features">
          <li><svg class="tick" viewBox="0 0 10 10"><circle cx="5" cy="5" r="4.2" fill="none" stroke="#1fa8e0"/><path d="M3 5.2l1.5 1.5L7.3 3.6" fill="none" stroke="#1fa8e0" stroke-width="1.2"/></svg>3-8 Staff Users</li>
          <li><svg class="tick" viewBox="0 0 10 10"><circle cx="5" cy="5" r="4.2" fill="none" stroke="#1fa8e0"/><path d="M3 5.2l1.5 1.5L7.3 3.6" fill="none" stroke="#1fa8e0" stroke-width="1.2"/></svg>2-3 Cash Registers</li>
          <li><svg class="tick" viewBox="0 0 10 10"><circle cx="5" cy="5" r="4.2" fill="none" stroke="#1fa8e0"/><path d="M3 5.2l1.5 1.5L7.3 3.6" fill="none" stroke="#1fa8e0" stroke-width="1.2"/></svg>1 Store Location</li>
        </ul>
      </div>
    </article>

    <article class="package package--foot">
      <div class="package-head"><div class="package-name">LARGE RETAIL</div><div class="package-sub">SOFTWARE PACKAGE</div></div>
      <div class="package-body">
        <div class="package-price"><span class="cur">$</span>34<sup>95</sup></div>
        <div class="package-week">Per Week</div>
        <ul class="package-features">
          <li><svg class="tick" viewBox="0 0 10 10"><circle cx="5" cy="5" r="4.2" fill="none" stroke="#1fa8e0"/><path d="M3 5.2l1.5 1.5L7.3 3.6" fill="none" stroke="#1fa8e0" stroke-width="1.2"/></svg>8-20 Staff Users</li>
          <li><svg class="tick" viewBox="0 0 10 10"><circle cx="5" cy="5" r="4.2" fill="none" stroke="#1fa8e0"/><path d="M3 5.2l1.5 1.5L7.3 3.6" fill="none" stroke="#1fa8e0" stroke-width="1.2"/></svg>2-10 Cash Registers</li>
          <li><svg class="tick" viewBox="0 0 10 10"><circle cx="5" cy="5" r="4.2" fill="none" stroke="#1fa8e0"/><path d="M3 5.2l1.5 1.5L7.3 3.6" fill="none" stroke="#1fa8e0" stroke-width="1.2"/></svg>1 Store Location</li>
        </ul>
      </div>
    </article>

    <article class="package package--foot">
      <div class="package-head"><div class="package-name">LARGE RETAIL PLUS</div><div class="package-sub">SOFTWARE PACKAGE</div></div>
      <div class="package-body">
        <div class="package-price"><span class="cur">$</span>49<sup>95</sup></div>
        <div class="package-week">Per Week</div>
        <ul class="package-features">
          <li><svg class="tick" viewBox="0 0 10 10"><circle cx="5" cy="5" r="4.2" fill="none" stroke="#1fa8e0"/><path d="M3 5.2l1.5 1.5L7.3 3.6" fill="none" stroke="#1fa8e0" stroke-width="1.2"/></svg>20+ Staff Users</li>
          <li><svg class="tick" viewBox="0 0 10 10"><circle cx="5" cy="5" r="4.2" fill="none" stroke="#1fa8e0"/><path d="M3 5.2l1.5 1.5L7.3 3.6" fill="none" stroke="#1fa8e0" stroke-width="1.2"/></svg>10+ Cash Registers</li>
          <li><svg class="tick" viewBox="0 0 10 10"><circle cx="5" cy="5" r="4.2" fill="none" stroke="#1fa8e0"/><path d="M3 5.2l1.5 1.5L7.3 3.6" fill="none" stroke="#1fa8e0" stroke-width="1.2"/></svg>2-3 Store Locations</li>
        </ul>
      </div>
    </article>
  </div>

  <footer class="back-contact">
    <div class="contact-phone">1300 462 718</div>
    <div class="contact-line">admin@vendraq7.com.au</div>
    <div class="contact-line">www.vendraq7.com.au</div>
  </footer>
</section>

<section class="flyer flyer--front" aria-label="Flyer front: features">
  <header class="front-head">
    <div class="front-brand">VENDRA Q7</div>
  </header>

  <ul class="feature-list">
    <li>Retail Point of Sale</li>
    <li>Hardware and Software</li>
    <li>Highly customisable to suit your business</li>
    <li>Free POS appraisal and Quotes</li>
    <li>E-commerce Integrations with your existing website</li>
    <li>Multiple Store Capability</li>
    <li>One on one set up and support</li>
  </ul>

  <svg class="front-foot" viewBox="0 0 520 200" aria-hidden="true">
    <polygon points="0,140 520,62 520,68 0,146" fill="var(--blue)"/>
    <polygon points="0,146 520,68 520,70 0,168" fill="var(--navy)"/>
    <polygon points="0,168 520,70 520,200 0,200" fill="var(--red)"/>
  </svg>
  <div class="tax-offer">
    <div class="tax-figure">100%</div>
    <div class="tax-label">Tax Deductable</div>
  </div>
</section>

</body>
</html>
```